BrQeL Upcycle Design - Infographic to depict upcycle program for furniture manufacturer

Essentially I need a graphic to go along with a great logo already created for us.Core aspects of our furniture brand are quality and environmental sustainability. In light of those two things we are creating an "upcycle" aspect of our business model. Customers can choose at a later date to Upcycle their furniture. We either help facilitate a swap to someone locally wanting good furniture OR we bring it back to the plant and remanufacture it. We keep from "wasting" this furniture that cane have another life. AND - the customer gets a credit back for future purchase with the company. Even if they are just moving to a new place and their current furniture won't fit - we can take it back and get it a new home and they can start fresh without completely wasting their investment or the vital natural resources in their furniture.....So I need some kind of BrQeL Upcycle graphic or "icon" that kind of visually sums up this concept

Target Market(s)

Young professionals and environmentally conscious consumers who want lasting quality and are opting out of the ""throw away" economy

Requirements
Must have
• Tie to the simplicity and "clean" lined nature of the company logos. Must quickly sum up the notions of "UpCycling" and environmental stewardship through quality remanufacturing products to have a new life rather then end up in landfill.

```html
<!DOCTYPE html>
<html lang="en">
<head>
<meta charset="UTF-8">
<title>BrQeL Upcycle</title>
<link rel="stylesheet" href="https://fonts.googleapis.com/css2?family=Montserrat:wght@400;600;700;800&display=swap">
<style>
  :root {
    --taupe: #9b8178;
    --taupe-dark: #7f6860;
    --sand: #bdae8f;
    --paper: #f2f2f3;
    --box-light: #efece6;
    --ink: #4a4043;
    --white: #ffffff;
    --canvas: #ffffff;
  }
  * { box-sizing: border-box; margin: 0; padding: 0; }
  html, body { width: 1200px; height: 849px; overflow: hidden; background: var(--canvas); }
  body { font-family: "Montserrat", sans-serif; color: var(--ink); position: relative; }
  .icon-defs { position: absolute; width: 0; height: 0; }

  /* ---------- Poster ---------- */
  .poster {
    position: absolute; left: 96px; top: 136px; width: 394px; height: 556px;
    background: var(--paper);
  }
  .poster__header {
    position: absolute; left: 0; top: 0; width: 100%; height: 101px;
    background: var(--taupe); display: flex; align-items: center; justify-content: center;
  }
  .poster__title { color: var(--white); font-weight: 800; font-size: 31px; letter-spacing: 1px; }
  .poster__frame {
    position: absolute; left: 27px; top: 104px; width: 343px; height: 395px;
    border: 3px solid var(--taupe);
  }
  .poster__art { position: absolute; left: 0; top: 0; width: 394px; height: 556px; }
  .poster__text { position: absolute; text-align: center; text-transform: uppercase; }
  .section-title { font-weight: 800; font-size: 13px; color: var(--ink); }
  .tiny-label { font-weight: 700; font-size: 5.5px; line-height: 1.3; color: var(--ink); }
  .body-note { font-weight: 600; font-size: 6px; line-height: 1.5; color: var(--ink); }
  .or-word { position: absolute; font-weight: 800; font-size: 15px; color: var(--ink); }

  .wordmark { position: absolute; font-weight: 700; text-transform: uppercase; letter-spacing: 0; }
  .poster .wordmark { right: 26px; top: 518px; font-size: 15px; color: var(--taupe-dark); }

  /* ---------- Landscape panel ---------- */
  .panel {
    position: absolute; left: 559px; top: 223px; width: 537px; height: 373px;
    background: var(--taupe);
  }
  .panel__lines { position: absolute; left: 0; top: 0; width: 537px; height: 373px; }
  .tile {
    position: absolute; width: 63px; height: 63px;
    display: flex; align-items: center; justify-content: center;
    outline: 2px solid var(--box-light); outline-offset: -5px;
  }
  .tile svg { width: 40px; height: 40px; }
  .tile--sand { background: var(--sand); color: var(--white); border: 2px solid var(--white); }
  .tile--light { background: var(--box-light); color: var(--taupe-dark); border: 2px solid var(--sand); outline: none; }
  .tile--hero { background: var(--sand); border: 2px solid var(--white); outline: none; }
  .tile__word { color: var(--white); font-weight: 700; font-size: 14px; line-height: 1.2; text-align: center; letter-spacing: 1px; }
  .panel__label {
    position: absolute; color: var(--white); font-weight: 700; font-size: 7px;
    line-height: 1.4; text-align: center; text-transform: uppercase; letter-spacing: .5px;
  }
  .panel .wordmark { left: 205px; top: 70px; font-size: 20px; color: var(--white); }
</style>
</head>
<body>

<svg class="icon-defs" aria-hidden="true">
  <defs>
    <symbol id="icon-diamond" viewBox="0 0 40 40">
      <g fill="none" stroke="currentColor" stroke-width="1.5" stroke-linejoin="round">
        <path d="M7 16 L13 9 H27 L33 16 L20 33 Z"/>
        <path d="M7 16 H33 M13 9 L17 16 L20 33 L23 16 L27 9"/>
        <path d="M33 4 V9 M30.5 6.5 H35.5"/>
      </g>
    </symbol>
    <symbol id="icon-recycle" viewBox="0 0 40 40">
      <g fill="none" stroke="currentColor" stroke-width="1.5" stroke-linejoin="round" stroke-linecap="round">
        <path d="M15 14 L19 8 Q20 6.5 21 8 L25 14"/>
        <path d="M22 13 L25 14 L26 11"/>
        <path d="M28 20 L32 27 Q33 29 31 29 H24"/>
        <path d="M26 26 L24 29 L27 31"/>
        <path d="M16 29 H9 Q7 29 8 27 L12 20"/>
        <path d="M9.5 21.5 L12 20 L13.5 23"/>
      </g>
    </symbol>
    <symbol id="icon-furniture" viewBox="0 0 40 40">
      <g fill="none" stroke="currentColor" stroke-width="1.5" stroke-linejoin="round">
        <rect x="4" y="19" width="17" height="8"/>
        <path d="M6 19 V13 H19 V19 M4 27 V30 M21 27 V30"/>
        <path d="M25 10 H33 V21 H25 Z M24 21 H34 V24 H24 Z M25 24 V32 M33 24 V32"/>
      </g>
    </symbol>
    <symbol id="icon-truck" viewBox="0 0 40 40">
      <g fill="none" stroke="currentColor" stroke-width="1.5" stroke-linejoin="round">
        <rect x="3" y="11" width="22" height="16"/>
        <path d="M25 16 H31 L36 22 V27 H25"/>
        <circle cx="10" cy="29" r="2.8"/>
        <circle cx="30" cy="29" r="2.8"/>
        <path d="M11 17 L14 14 L17 17 M18 21 L16 24 H12 M10 22 L11 18"/>
      </g>
    </symbol>
    <symbol id="icon-credit" viewBox="0 0 40 40">
      <g fill="none" stroke="currentColor" stroke-width="1.5" stroke-linejoin="round" stroke-linecap="round">
        <rect x="14" y="6" width="20" height="13" rx="1.5"/>
        <path d="M14 10 H34 M17 15 H22"/>
        <path d="M4 30 H10 L19 33 L33 26 Q35 24 32 24 L24 27 H17"/>
        <path d="M10 30 V24 H15 L22 25 Q24 26 22 27"/>
      </g>
    </symbol>
    <symbol id="icon-factory" viewBox="0 0 40 40">
      <g fill="none" stroke="currentColor" stroke-width="1.5" stroke-linejoin="round">
        <path d="M5 34 V21 L12 16 V21 L19 16 V21 L26 16 V34 Z"/>
        <path d="M26 34 V9 H31 V34 Z M3 34 H36"/>
        <rect x="9" y="26" width="4" height="4"/>
        <rect x="17" y="26" width="4" height="4"/>
      </g>
    </symbol>
  </defs>
</svg>

<section class="poster" aria-label="Upcycle poster">
  <header class="poster__header"><h1 class="poster__title">UPCYCLE</h1></header>
  <div class="poster__frame"></div>

  <svg class="poster__art" viewBox="0 0 394 556" aria-hidden="true">
    <g stroke="var(--taupe)" stroke-width="1.2" fill="none">
      <line x1="173" y1="186" x2="216" y2="186"/>
      <line x1="195" y1="186" x2="195" y2="222"/>
      <line x1="197" y1="272" x2="197" y2="290"/>
      <line x1="133" y1="358" x2="267" y2="358"/>
      <line x1="133" y1="358" x2="198" y2="436"/>
      <line x1="267" y1="358" x2="198" y2="436"/>
    </g>
    <g fill="var(--taupe)">
      <circle cx="152" cy="186" r="21"/>
      <circle cx="237" cy="186" r="21"/>
    </g>
    <use href="#icon-diamond" x="138" y="172" width="28" height="28" style="color:var(--white)"/>
    <use href="#icon-recycle" x="223" y="172" width="28" height="28" style="color:var(--white)"/>
    <g fill="var(--paper)" stroke="var(--taupe)" stroke-width="1.6">
      <circle cx="133" cy="358" r="31"/>
      <circle cx="267" cy="358" r="31"/>
      <circle cx="198" cy="436" r="31"/>
      <circle cx="198" cy="357" r="17"/>
    </g>
    <g style="color:var(--taupe-dark)">
      <use href="#icon-furniture" x="113" y="338" width="40" height="40"/>
      <use href="#icon-factory" x="247" y="338" width="40" height="40"/>
      <use href="#icon-credit" x="178" y="416" width="40" height="40"/>
      <use href="#icon-truck" x="186" y="345" width="24" height="24"/>
    </g>
  </svg>

  <p class="poster__text section-title" style="left:0;width:394px;top:113px;">Our core aspects</p>
  <p class="poster__text tiny-label" style="left:122px;width:60px;top:158px;">Quality</p>
  <p class="poster__text tiny-label" style="left:202px;width:70px;top:152px;">Environmental<br>Sustainability</p>
  <p class="poster__text section-title" style="left:0;width:394px;top:226px;">Our model</p>
  <p class="poster__text body-note" style="left:112px;width:170px;top:250px;">Customers can choose at a later<br>date to upcycle their furniture.</p>
  <p class="poster__text body-note" style="left:68px;width:130px;top:300px;">We help facilitate a<br>swap to good home</p>
  <span class="or-word" style="left:190px;top:302px;">or</span>
  <p class="poster__text body-note" style="left:205px;width:130px;top:300px;">You bring it back to the plant<br>and we remanufacture it</p>
  <p class="poster__text body-note" style="left:112px;width:170px;top:468px;">You get a credit back for future<br>purchase with BrQeL</p>

  <p class="wordmark">BrQeL</p>
</section>

<section class="panel" aria-label="Upcycle diagram">
  <svg class="panel__lines" viewBox="0 0 537 373" aria-hidden="true">
    <g stroke="var(--white)" stroke-width="1.6" fill="none">
      <line x1="129" y1="115" x2="165" y2="150"/>
      <line x1="129" y1="239" x2="165" y2="209"/>
      <line x1="226" y1="180" x2="251" y2="180"/>
      <line x1="314" y1="180" x2="339" y2="180"/>
      <line x1="402" y1="160" x2="432" y2="111"/>
      <line x1="402" y1="200" x2="432" y2="251"/>
    </g>
  </svg>

  <p class="panel__label" style="left:56px;width:84px;top:29px;">Quality</p>
  <div class="tile tile--sand" style="left:66px;top:52px;"><svg aria-hidden="true"><use href="#icon-diamond"/></svg></div>

  <div class="tile tile--sand" style="left:66px;top:239px;"><svg aria-hidden="true"><use href="#icon-recycle"/></svg></div>
  <p class="panel__label" style="left:38px;width:120px;top:318px;">Environmental<br>Sustainability</p>

  <div class="tile tile--hero" style="left:163px;top:148px;"><span class="tile__word">UP<br>CY<br>CLE</span></div>
  <div class="tile tile--light" style="left:251px;top:148px;"><svg aria-hidden="true"><use href="#icon-furniture"/></svg></div>
  <div class="tile tile--light" style="left:339px;top:148px;"><svg aria-hidden="true"><use href="#icon-truck"/></svg></div>
  <div class="tile tile--light" style="left:422px;top:47px;width:64px;height:66px;"><svg aria-hidden="true"><use href="#icon-credit"/></svg></div>
  <div class="tile tile--light" style="left:422px;top:249px;width:64px;height:66px;"><svg aria-hidden="true"><use href="#icon-factory"/></svg></div>

  <p class="wordmark">BrQeL</p>
</section>

</body>
</html>
```